Creating a page for our Spanish tutoring service

We recently launched a new service and would like to create new "solutions" pages to add to our website.

Previously, we provided private one-on-one Spanish tutoring. Now, we are also providing group classes.

We have two documents with some basic copy on each offering. Our website is nice and does not require changes currently, but we do not have the internal bandwidth to build these pages. You would be using our existing design elements to build these two web pages.

Repurposing/copying blocks from our other pages is fine! We have a developer, so design only is required. If you do a good job on this first project, we will have many more pages and projects for you to do!

Our website is lingotrail.com. TIA for any applicants.

---

Private classes copy:
https://files.quorvant.net/doc/7KqP2mZx9Lr4Wn8Tb3Vy6Hs1Jd5Fc0Ng/view

Group classes copy:
https://files.quorvant.net/doc/3Rb8Yt6Km1Xp9Qz4Ls7Gv2Nc5Wh0Dj8E/view

Target Market(s)

Online Spanish tutoring and online Spanish classes. We are a very high quality, yet affordable service. Our unique selling proposition is that we operate a completely remote team.

Current customers are typically well-to-do parents or professionals who want to learn Spanish for fun or personal development. They are usually in an okay standing financially (or want to be).

Those who pay for their kids to take lessons want them to have a better future or communicate with their families. Those who are young typically subscribe because they want a better future for themselves. Those who are 30+ years old learn for leisure, travel, or for ongoing professional development.

They want a quality product without paying the high costs associated with in-person tutoring, which is significantly more expensive. They also want to avoid cheaper solutions that are low cost but conversely low quality.

Number of Pages Required

2 page

Font styles to use
Other font styles liked:
• Avenir is our font

Requirements
Must have
• A look and feel consistent with the rest of our website.

```html
<!DOCTYPE html>
<html lang="en">
<head>
<meta charset="utf-8">
<title>LingoTrail – Online Spanish Tutoring</title>
<link rel="stylesheet" href="https://fonts.googleapis.com/css2?family=Nunito+Sans:wght@400;600;700;800&display=swap">
<style>
:root{
  --teal:#52b5a8;
  --teal-light:#6cc1b7;
  --teal-dark:#3aa597;
  --orange:#ff7a45;
  --ink:#333c4a;
  --ink-soft:#4a4f57;
  --muted:#6b6f75;
  --grey-bg:#eef3f3;
  --footer-bg:#f8f3f1;
  --white:#ffffff;
}
*{box-sizing:border-box;margin:0;padding:0}
html,body{width:1200px;height:2224px;overflow:hidden}
body{font-family:"Nunito Sans",Arial,sans-serif;color:var(--ink);background:var(--white);position:relative}
.abs{position:absolute}

/* hero */
.hero{left:0;top:0;width:1200px;height:571px;background:var(--teal)}
.brand{display:flex;align-items:center;gap:6px;color:var(--white);font-weight:700;font-size:15px;letter-spacing:.5px}
.brand-mark{width:10px;height:10px;background:var(--orange)}
.nav-link{color:var(--white);font-size:10px;font-weight:800;text-transform:uppercase;top:26px}
.btn-start{left:865px;top:14px;width:125px;height:27px;border-radius:14px;background:var(--orange);color:var(--white);font-size:10px;font-weight:800;display:flex;align-items:center;justify-content:center}
.hero-title{left:0;width:1200px;top:88px;text-align:center;color:var(--white);font-size:28px;font-weight:800}
.hero-art{left:402px;top:167px;width:373px;height:239px;border-radius:8px;background:linear-gradient(135deg,#2f3b45 0%,#e9f2f2 40%,#1f4fb0 80%,#3d8fd8 100%)}
.hero-sub{left:0;width:1200px;top:410px;text-align:center;color:var(--white);font-size:15.5px;font-weight:800}
.btn-trial{left:481px;top:448px;width:210px;height:62px;border-radius:12px;background:var(--orange);color:var(--white);font-size:23px;font-weight:700;display:flex;align-items:center;justify-content:center}
.dot{top:521px;width:4px;height:4px;border-radius:50%}

/* features */
.feature{top:652px;width:300px}
.feature h3{text-align:center;font-size:21px;font-weight:700;color:var(--ink-soft);margin-bottom:16px}
.feature p{font-size:17px;line-height:22px;text-align:justify;color:var(--ink-soft)}

/* why */
.why-band{left:0;top:852px;width:1200px;height:426px;background:var(--grey-bg)}
.why-copy{left:44px;top:896px;width:540px;font-size:15px;line-height:19.3px;font-weight:700;color:var(--ink-soft);text-align:justify}
.why-copy p{margin-bottom:19px}
.why-art{left:743px;top:949px;width:380px;height:177px;border-radius:6px;background:linear-gradient(90deg,#e8873a 0%,#27c6ad 40%,#2b3a4a 75%,#eef3f3 100%)}

/* stories */
.stories-band{left:0;top:1278px;width:1200px;height:359px;background:var(--teal-light)}
.stories-title{left:0;width:1200px;top:1292px;text-align:center;color:var(--white);font-size:25px;font-weight:700}
.stories-sub{left:370px;width:460px;top:1329px;text-align:center;color:var(--white);font-size:12.3px;line-height:18px}
.story{top:1406px;width:218px;background:var(--white);box-shadow:0 2px 6px rgba(0,0,0,.06)}
.story-photo{height:230px;position:relative}
.play{position:absolute;left:79px;top:85px;width:60px;height:60px;border-radius:50%;background:var(--white);display:flex;align-items:center;justify-content:center}
.story-info{padding:14px 15px 12px;font-size:12.3px;line-height:22.5px}
.story-info div{display:flex}
.story-info b{width:84px;color:var(--ink);font-weight:700}
.story-info span{color:var(--muted)}

/* group */
.group-title{left:44px;top:1816px;width:540px;font-size:24.5px;line-height:29px;font-weight:700;color:var(--ink-soft);text-align:justify}
.group-copy{left:44px;top:1922px;width:540px;font-size:15px;line-height:19.3px;font-weight:700;color:var(--ink-soft)}
.btn-group{left:770px;top:1829px;width:298px;height:88px;border-radius:14px;background:var(--teal-dark);color:var(--white);font-size:21px;line-height:26px;font-weight:700;text-align:center;display:flex;align-items:center;justify-content:center}

/* footer */
.footer{left:0;top:1990px;width:1200px;height:234px;background:var(--footer-bg)}
.foot-col{top:2034px;font-size:11.5px;line-height:19px;color:var(--muted)}
.foot-col h4{font-size:13.5px;font-weight:600;color:var(--ink);margin-bottom:3px}
.social{top:2085px;width:24px;height:24px;border-radius:50%}
.foot-brand{left:383px;top:2156px;color:var(--teal);font-weight:700;font-size:14px;letter-spacing:.5px}
.copyright{left:489px;top:2159px;font-size:10.5px;color:var(--muted)}
.copyright u{color:#2a4fa8}
</style>
</head>
<body>

<header class="abs hero"></header>
<div class="abs brand" style="left:180px;top:22px"><span class="brand-mark"></span>LingoTrail</div>
<span class="abs nav-link" style="left:307px">How it works</span>
<span class="abs nav-link" style="left:417px">Teachers</span>
<span class="abs nav-link" style="left:501px">Testimonials</span>
<span class="abs nav-link" style="left:606px">Pricing</span>
<span class="abs nav-link" style="left:681px">About us</span>
<a class="abs btn-start">GET STARTED</a>

<h1 class="abs hero-title">Award-Winning Online Spanish Tutoring</h1>
<div class="abs hero-art" role="img" aria-label="Illustration of a student at a desk joining a video lesson with a tutor on screen"></div>
<p class="abs hero-sub">Expert online Spanish tutoring for all levels</p>
<a class="abs btn-trial">Try a free class</a>
<span class="abs dot" style="left:579px;background:#24504a"></span>
<span class="abs dot" style="left:605px;background:#3e8b81"></span>

<section>
  <div class="abs feature" style="left:48px">
    <h3>Expert Teachers</h3>
    <p>LingoTrail teachers are trained in the science of teaching Spanish and have worked thousands of hours helping Spanish learners globally.</p>
  </div>
  <div class="abs feature" style="left:444px">
    <h3>Dedicated Attention</h3>
    <p>Accelerate your learning with one-on-one classes featuring a curriculum that’s custom built for your unique needs and interests.</p>
  </div>
  <div class="abs feature" style="left:840px">
    <h3>Flexible and Convenient</h3>
    <p>Online tutoring allows you to learn whenever, and wherever. Find time to continue learning, even if you have a tight schedule.</p>
  </div>
</section>

<div class="abs why-band"></div>
<div class="abs why-copy">
  <p>Why Private Spanish Tutoring?</p>
  <p>Fast-track your language learning using online Spanish classes with a dedicated teacher. Get an effective curriculum that’s built around your specific goals and current level of comprehension.</p>
  <p>What kinds of classes can you expect?</p>
  <p>Conversational Want to get ready for conversations in the real world? Lessons on every-day topics can help build your vocabulary in essential areas and help you build more confidence speaking.</p>
  <p>Grammar Learn the basics or perfect your grammar for use in personal or professional settings. Our grammar-oriented lessons will build you vocabulary while helping you speak perfectly like a native.</p>
</div>
<div class="abs why-art" role="img" aria-label="Illustration of a study desk with books, a monitor showing a graduation cap, pencils and a desk lamp"></div>

<div class="abs stories-band"></div>
<h2 class="abs stories-title">Success Stories</h2>
<p class="abs stories-sub">At the core of every business is a great success story. Here we bring you a collection of stories highlighting how LingoTrail has contributed to students all over the world in becoming conversational or fluent in Spanish.</p>

<div class="abs story" style="left:250px">
  <div class="story-photo" role="img" aria-label="Video still of student Marco" style="background:linear-gradient(180deg,#d9dadb,#8a7a70 60%,#3f4042)">
    <span class="play"><svg width="22" height="24" viewBox="0 0 22 24"><path d="M2 1 L21 12 L2 23 Z" fill="#7b6b66"/></svg></span>
  </div>
  <div class="story-info"><div><b>Students:</b><span>Marco</span></div><div><b>Tutor:</b><span>Ramiro</span></div><div><b>Plan:</b><span>Conversational</span></div></div>
</div>
<div class="abs story" style="left:495px">
  <div class="story-photo" role="img" aria-label="Video still of student Dana" style="background:linear-gradient(180deg,#e9e3c8,#6a4a3a 55%,#8c93b0)">
    <span class="play"><svg width="22" height="24" viewBox="0 0 22 24"><path d="M2 1 L21 12 L2 23 Z" fill="#c59a8c"/></svg></span>
  </div>
  <div class="story-info"><div><b>Students:</b><span>Dana</span></div><div><b>Tutor:</b><span>Lucía</span></div><div><b>Plan:</b><span>Fluent</span></div></div>
</div>
<div class="abs story" style="left:740px">
  <div class="story-photo" role="img" aria-label="Video still of student Harper" style="background:linear-gradient(180deg,#25a6c8,#8a6a50 55%,#d8d4cc)">
    <span class="play"><svg width="22" height="24" viewBox="0 0 22 24"><path d="M2 1 L21 12 L2 23 Z" fill="#b88a78"/></svg></span>
  </div>
  <div class="story-info"><div><b>Students:</b><span>Harper</span></div><div><b>Tutor:</b><span>Elena</span></div><div><b>Plan:</b><span>Conversational</span></div></div>
</div>

<h2 class="abs group-title">Group classes are also available OR Try group classes instead</h2>
<p class="abs group-copy">Led by our certified teachers, group classes give learners the opportunity to have real, interactive conversations in Spanish with their peers.</p>
<a class="abs btn-group">Learn more about group<br>classes</a>

<footer class="abs footer"></footer>
<div class="abs foot-col" style="left:170px"><h4>Information</h4>How It Works<br>Pricing</div>
<div class="abs foot-col" style="left:315px"><h4>Service</h4>Teachers<br>Testimonials</div>
<div class="abs foot-col" style="left:461px"><h4>Company</h4>About Us<br>Become an affiliate</div>
<div class="abs foot-col" style="left:606px"><h4>Legal</h4>Privacy policy<br>Terms of use</div>
<div class="abs foot-col" style="left:897px"><h4>Get in touch</h4>Contact Support</div>
<span class="abs social" style="left:897px;background:#3b5a9a" aria-label="Social profile"></span>
<span class="abs social" style="left:929px;background:#e0407a" aria-label="Social profile"></span>
<div class="abs foot-brand">LingoTrail</div>
<p class="abs copyright">Copyright © 2020 LingoTrail, Inc. All rights reserved. <u>Privacy Policy</u>.</p>

</body>
</html>
```